Upmarket Dessert Lounge needs a Business Card Design

We are an upmarket dessert lounge needing a business card to match our image.

We want something that is simple yet beautiful, feminine, classy, sophisticated and elegant. We want it to stand out and don't mind if it is bold.

The design should include our logo and colours of red or maroon with gold highlights. We don't mind if black is used.

Marlow & Quince

Target Market(s)

For those who like to indulge or treat themselves and give in to their temptations on good quality desserts.

Industry/Entity Type

Business

Requirements
Must have
• Must include our logo and our name

Marlow & Quince

M & Q

```html
<!DOCTYPE html>
<html lang="en">
<head>
<meta charset="utf-8">
<title>Marlow &amp; Quince — Business Card</title>
<link rel="stylesheet" href="https://fonts.googleapis.com/css2?family=Cormorant+Garamond:wght@500;600&family=Cinzel:wght@500&display=swap">
<style>
  :root {
    --backdrop: #2f2f30;
    --card-black: #151515;
    --band-red: #7e1013;
    --band-red-dark: #5e0b0e;
    --gold: #e9c98d;
    --gold-soft: #cfae72;
  }
  html, body {
    margin: 0;
    width: 1200px;
    height: 900px;
    overflow: hidden;
    background: var(--backdrop);
  }
  .canvas {
    position: relative;
    width: 1200px;
    height: 900px;
  }
  .card {
    position: absolute;
    left: 290px;
    width: 620px;
    height: 354px;
    background: var(--card-black);
    box-shadow: 0 10px 28px rgba(0,0,0,.45);
    overflow: hidden;
  }
  .card--front { top: 64px; }
  .card--back  { top: 482px; }

  .band {
    position: absolute;
    top: 0;
    bottom: 0;
    background: var(--band-red);
    display: flex;
    align-items: center;
    justify-content: center;
  }
  .card--front .band { left: 150px; width: 200px; }
  .card--back  .band { left: 40px;  width: 190px; }

  .brand {
    display: flex;
    flex-direction: column;
    align-items: center;
    gap: 10px;
    font-family: "Cinzel", serif;
    font-weight: 500;
    color: var(--gold);
    text-align: center;
    line-height: 1.05;
    letter-spacing: .06em;
  }
  .brand__mark {
    width: 14px;
    height: 14px;
    border-radius: 50%;
    background: var(--gold);
  }
  .card--front .brand__name { font-size: 30px; }
  .card--back  .brand__name { font-size: 25px; }

  .website {
    font-family: "Cormorant Garamond", serif;
    font-weight: 600;
    color: var(--gold);
    letter-spacing: .22em;
  }
  .card--front .website {
    position: absolute;
    left: 370px;
    top: 50%;
    transform: translateY(-50%);
    font-size: 17px;
    letter-spacing: .16em;
  }

  .details {
    position: absolute;
    left: 268px;
    top: 96px;
    font-family: "Cormorant Garamond", serif;
    font-weight: 500;
    color: var(--gold);
  }
  .details__name {
    font-size: 22px;
    letter-spacing: .08em;
    text-transform: uppercase;
    margin: 0;
  }
  .details__role {
    font-size: 13px;
    margin: 2px 0 12px;
    color: var(--gold-soft);
  }
  .details__line {
    font-size: 13px;
    margin: 0 0 4px;
    color: var(--gold-soft);
  }
  .details .website {
    font-size: 17px;
    margin-top: 12px;
  }
</style>
</head>
<body>
<main class="canvas">

  <section class="card card--front" aria-label="Card front">
    <div class="band">
      <div class="brand">
        <span class="brand__mark"></span>
        <span class="brand__name">Marlow<br>&amp;<br>Quince</span>
      </div>
    </div>
    <p class="website">www.Marlow-Quince.com</p>
  </section>

  <section class="card card--back" aria-label="Card back">
    <div class="band">
      <div class="brand">
        <span class="brand__mark"></span>
        <span class="brand__name">Marlow<br>&amp;<br>Quince</span>
      </div>
    </div>
    <div class="details">
      <p class="details__name">Clara Whitby</p>
      <p class="details__role">Manager</p>
      <p class="details__line">m: + 123 555 0190 / f: + 123 555 0190</p>
      <p class="details__line">e: clara@marlow-quince.com</p>
      <p class="website">www.marlow-quince.com</p>
    </div>
  </section>

</main>
</body>
</html>
```